Business cards for Keelwind Consulting (Leadership & Performance Coaching and HR Consulting)

I have a logo (although I'm open to new ideas) and I need this added to a business card. Ultimately, I will also need help with a website. This is an independent consulting firm that is focuses on Leadership, Performance, Executive Coaching and Talent.
Google the story about "a storm, a pilot" ... hence the Keelwind

Target Market(s)

My clients, CEOs, CHROs, COOs

Contact Information for Business Card

Nora T. Vale
President
503.555.0173
nvale52@brightmailbox.net
www.keelwindconsulting.net
5318 Harrowgate Dr., Lindell, OR 97388

Font styles to use
Serif
Sans Serif

Colors
ec1f27
0455a3

Requirements
Must have
• Color, be professional
Nice to have
• Something that pops off the card
Should not have
• Be boring.

```html
<!DOCTYPE html>
<html lang="en">
<head>
<meta charset="utf-8">
<title>Keelwind Consulting – Business Card</title>
<link rel="stylesheet" href="https://fonts.googleapis.com/css2?family=Roboto:wght@400;500;700&display=swap">
<style>
  :root {
    --page-bg: #e6e1d8;
    --card-bg: #030608;
    --brand-red: #e41f27;
    --brand-blue: #3a52a6;
    --tab-blue: #3a52a6;
    --accent-blue: #4aa6e0;
    --body-text: #d8d8d8;
  }
  * { margin: 0; padding: 0; box-sizing: border-box; }
  html, body {
    width: 1125px;
    height: 1200px;
    overflow: hidden;
    background: var(--page-bg);
    font-family: "Roboto", Arial, sans-serif;
  }
  .canvas {
    position: relative;
    width: 1125px;
    height: 1200px;
  }
  .card {
    position: absolute;
    left: 171px;
    width: 826px;
    height: 471px;
    background: var(--card-bg);
    box-shadow: 0 4px 10px rgba(0, 0, 0, 0.35);
    overflow: hidden;
  }
  .card--front { top: 106px; }
  .card--back { top: 639px; }

  .accent-tab {
    position: absolute;
    left: 558px;
    top: 0;
    width: 117px;
    height: 92px;
    background: var(--tab-blue);
  }
  .firm-name {
    position: absolute;
    right: 51px;
    top: 178px;
    color: var(--accent-blue);
    font-weight: 500;
    font-size: 32px;
    letter-spacing: 1px;
    text-transform: uppercase;
    white-space: nowrap;
  }
  .firm-tagline {
    position: absolute;
    right: 51px;
    top: 216px;
    color: var(--accent-blue);
    font-weight: 500;
    font-size: 16px;
    letter-spacing: 1.6px;
    text-transform: uppercase;
    white-space: nowrap;
  }

  .contact {
    position: absolute;
    left: 37px;
    top: 222px;
  }
  .contact__name {
    color: var(--brand-blue);
    font-weight: 700;
    font-size: 29px;
    line-height: 34px;
    text-transform: uppercase;
  }
  .contact__title {
    color: var(--brand-red);
    font-weight: 500;
    font-size: 20px;
    line-height: 24px;
    text-transform: uppercase;
  }
  .contact__block {
    margin-top: 18px;
    color: var(--body-text);
    font-size: 19px;
    line-height: 25px;
    font-style: normal;
  }
  .contact__block + .contact__block { margin-top: 12px; }

  .back-mark {
    position: absolute;
    right: 44px;
    top: 287px;
    display: flex;
    align-items: center;
    gap: 18px;
  }
  .back-mark__dot {
    width: 150px;
    height: 150px;
    border-radius: 50%;
    background: var(--brand-blue);
  }
  .back-mark__name {
    color: var(--accent-blue);
    font-weight: 500;
    font-size: 22px;
    letter-spacing: 1px;
    text-transform: uppercase;
  }
</style>
</head>
<body>
<main class="canvas">
  <section class="card card--front">
    <div class="accent-tab"></div>
    <div class="firm-name">Keelwind Consulting</div>
    <div class="firm-tagline">Coaching and Talent Strategy</div>

    <div class="contact">
      <h1 class="contact__name">Nora T. Vale</h1>
      <p class="contact__title">President</p>
      <address class="contact__block">
        5318 Harrowgate Dr.<br>
        Lindell, OR 97388
      </address>
      <p class="contact__block">
        P: 503.555.0173<br>
        nvale52@brightmailbox.net<br>
        www.keelwindconsulting.net
      </p>
    </div>
  </section>

  <section class="card card--back">
    <div class="back-mark">
      <span class="back-mark__name">Keelwind Consulting</span>
      <div class="back-mark__dot"></div>
    </div>
  </section>
</main>
</body>
</html>
```